Roofing Company Business Card Design

My husband and I own our own roofing company. We specialise in the supply and installation of metal roofing, fascia, gutter, and downpipes.
I would like our design to somehow incorporate the above things. Having said that the logo also needs to be versatile. I need to be able to use it for uniforms, signage for building sites, and also signage for our cars. So I need it to look good on both a small and large scale.
Looking at logo styles I would like to use either pictorial/combination logo, or emblem logo. With this I would like to try and incorporate the initials "TMR" into this logo somehow.
I would like to use blue, black, and white as my colours.
Industry/Entity Type
Building
Logo Text
Tallow Metal Roofing Pty Ltd
Logo styles of interest
Emblem Logo
Pictorial/Combination Logo
Look and feel

```html
<!DOCTYPE html>
<html lang="en">
<head>
<meta charset="utf-8">
<title>Tallow Metal Roofing – Business Card</title>
<link href="https://fonts.googleapis.com/css2?family=Exo+2:wght@500;600;700;800&display=swap" rel="stylesheet">
<style>
  :root{
    --backdrop:#ece8e2;
    --navy:#0b1a8c;
    --ink:#3a3a3a;
    --white:#ffffff;
    --steel-light:#c9cbce;
    --slate-top:#585858;
    --slate-bottom:#adadad;
  }
  *{box-sizing:border-box;margin:0;padding:0}
  html,body{width:1200px;height:899px;overflow:hidden}
  body{background:var(--backdrop);font-family:"Exo 2",sans-serif;position:relative}

  .card{position:absolute;width:520px;height:298px;overflow:hidden}
  .card--front{left:150px;top:137px;background:var(--white);border:1px solid #d8d8d8}
  .card--back{left:527px;top:460px;background:linear-gradient(180deg,var(--slate-top),var(--slate-bottom))}

  .card__band{position:absolute;left:0;top:0;width:520px;height:298px}

  .brand{position:absolute;display:flex;align-items:center;gap:10px}
  .brand__dot{flex:none;border-radius:50%}
  .brand__name{font-weight:700;line-height:1.15}

  .card--front .brand{left:26px;top:70px;width:200px}
  .card--front .brand__dot{width:22px;height:22px;background:var(--navy)}
  .card--front .brand__name{font-size:22px;color:var(--navy)}

  .card--back .brand{left:50%;top:96px;transform:translateX(-50%);white-space:nowrap}
  .card--back .brand__dot{width:24px;height:24px;background:var(--white)}
  .card--back .brand__name{font-size:28px;color:var(--white)}

  .person{position:absolute;left:262px;top:84px;width:240px;text-align:center}
  .person__name{font-size:25px;font-weight:700;color:var(--navy);line-height:30px}
  .person__role{font-size:15px;font-weight:600;color:var(--ink);letter-spacing:.18em;line-height:20px}

  .contact{position:absolute;left:0;top:232px;width:520px;text-align:center;color:var(--white);font-size:12.5px;font-weight:600;line-height:19px;letter-spacing:.02em}

  .services{position:absolute;left:0;top:228px;width:520px;text-align:center;color:var(--white);font-size:14px;font-weight:700;line-height:20px}
</style>
</head>
<body>

<section class="card card--front" aria-label="Business card front">
  <svg class="card__band" viewBox="0 0 520 298" aria-hidden="true">
    <defs>
      <linearGradient id="bandBlue" x1="0" y1="0" x2="0" y2="1">
        <stop offset="0" stop-color="#1a2fbf"/>
        <stop offset="1" stop-color="#06106a"/>
      </linearGradient>
      <linearGradient id="arcSteel" x1="0" y1="0" x2="1" y2="0">
        <stop offset="0" stop-color="#d9d9d9"/>
        <stop offset=".5" stop-color="#7d7f83"/>
        <stop offset="1" stop-color="#d9d9d9"/>
      </linearGradient>
    </defs>
    <path d="M0 180 Q260 150 520 180 L520 174 Q260 140 0 174 Z" fill="url(#arcSteel)"/>
    <path d="M0 186 Q260 160 520 186 L520 298 L0 298 Z" fill="url(#bandBlue)"/>
  </svg>

  <div class="brand">
    <span class="brand__dot"></span>
    <span class="brand__name">Tallow Metal Roofing</span>
  </div>

  <div class="person">
    <p class="person__name">Jenna Tallow</p>
    <p class="person__role">DIRECTOR</p>
  </div>

  <div class="contact">
    <p>Phone: 0400172936</p>
    <p>Email: jennatallow@mailbox.com</p>
  </div>
</section>

<section class="card card--back" aria-label="Business card back">
  <div class="brand">
    <span class="brand__dot"></span>
    <span class="brand__name">Tallow Metal Roofing</span>
  </div>

  <div class="services">
    <p>Specialising in the Installation of Metal Roofs,</p>
    <p>Fascia, Gutter, and Downpipes</p>
  </div>
</section>

</body>
</html>
```